Powerpoint Design for business and consulting company - Dorneck-Saalig

I am searching a design specialist who can help me to create a PowerPoint Design for my company. I'm in the business coaching and consulting industry.

The PPT master should be easy to use and include professional formatting (using the fonts of my website). In general, the slide master should have the look and feel of my website (in terms of fonts, colors, logos, possibility to place big photographs, having text and graph slides as well as photo slides with just 1 key message).

The PowerPoint design should fit my cooperate Identity (please see my website https://dorneck-saalig.de).
My logos are attached.

Additional information:
- wide screen format - 16: 9
- right set up of a fitting color scheme
https: // farbwexo. io / f6ded1-bfcbce-807f84-9cd3d1-666666
# 666666 (Dim Gray) - body / heading text
# 807F84 (Gray Web)
#BFCBCE (Silver Sand) - link hover
# 9cd3d1 (Powder Blue) - Link color
# F6DED1 (Champagne Pink)

- creation of chart templates, using chart tools, and different chart types etc.
- creation of different slide layouts to place content, pictures (in different sizes), optionally Media
- set up of display guide lines
- as well as standard elements, such as text boxes, lines, default shapes, etc.

Requirements
Must have
• Powerpoint Design needs to have:
https://farbwexo.io/f6ded1-bfcbce-807f84-9cd3d1-666666
# 807F84 (Gray Web)
# F6DED1 (Champagne Pink)

```html
<!DOCTYPE html>
<html lang="de">
<head>
<meta charset="utf-8">
<title>Dorneck-Saalig – Präsentationsvorlage</title>
<link href="https://fonts.googleapis.com/css2?family=Lato:ital,wght@0,300;0,400;0,700;1,400&family=Montserrat:wght@300;400;500&family=Playfair+Display:wght@400&display=swap" rel="stylesheet">
<style>
:root{
  --dim-gray:#666666;
  --gray-web:#807f84;
  --gray-soft:#9e9da1;
  --silver-sand:#bfcbce;
  --powder-blue:#9cd3d1;
  --champagne:#f6ded1;
  --peach:#f2a27c;
  --panel:#e3e1dd;
  --panel-dark:#d9d7d2;
  --white:#ffffff;
}
*{margin:0;padding:0;box-sizing:border-box}
html,body{width:900px;height:1200px;overflow:hidden;background:var(--white)}
body{position:relative;font-family:"Lato",sans-serif;color:var(--dim-gray)}
.slide{position:absolute;width:500px;height:281px;background:var(--white);overflow:hidden;transform-origin:0 0;transform:scale(.5425);box-shadow:0 4px 14px rgba(0,0,0,.28)}
.slide--title{width:765px;height:431px}
.abs{position:absolute}
.photo{position:absolute}
.brand{position:absolute;font-family:"Lato",sans-serif;font-weight:400;font-size:9px;letter-spacing:.2px;color:var(--dim-gray);white-space:nowrap;display:flex;align-items:center;gap:4px}
.brand::before{content:"";width:7px;height:7px;border-radius:50%;background:currentColor}
.brand--light{color:var(--white)}
.page{position:absolute;right:28px;bottom:10px;font-size:5.5px;color:var(--dim-gray)}
.heading{font-family:"Montserrat",sans-serif;font-weight:400;color:var(--gray-web)}
.hashtag{font-family:"Montserrat",sans-serif;font-weight:500;color:var(--peach)}
.body-copy{font-size:4.6px;line-height:1.45;text-align:justify;color:var(--gray-web)}
.quote{font-style:italic;color:var(--gray-web)}
.rule{position:absolute;height:1.5px;background:var(--gray-web)}
</style>
</head>
<body>

<!-- Title slide -->
<section class="slide slide--title" style="left:242.5px;top:34.7px">
  <div class="abs" style="left:0;top:0;width:382px;height:431px;background:var(--gray-web)"></div>
  <div class="photo" role="img" aria-label="Coach sitting on outdoor stone steps beside a railing, smiling" style="left:33px;top:33px;width:700px;height:365px;background:linear-gradient(120deg,#8fa9ab 0%,#6f7d7c 35%,#a58f7e 60%,#5d5a55 100%)"></div>
  <div class="brand brand--light" style="left:48px;top:48px;font-size:22px;font-weight:300;gap:10px">carola<br>dorneck-saalig</div>
  <div class="abs" style="left:240px;top:268px;width:460px;text-align:center;color:var(--white);font-family:'Montserrat',sans-serif;font-weight:300;line-height:1.25">
    <div style="font-size:18px">YOUR TITLE PRESENTATION GOES HERE</div>
    <div style="font-size:18px">Subtitle goes here</div>
    <div style="font-size:18px">Date Sept 2020</div>
  </div>
</section>

<!-- Welcome -->
<section class="slide" style="left:16.3px;top:303.8px">
  <div class="abs" style="left:245px;top:0;width:255px;height:281px;background:var(--gray-web)"></div>
  <div class="abs" style="left:18px;top:20px;width:272px;height:243px;background:var(--panel-dark);box-shadow:0 2px 6px rgba(0,0,0,.2)"></div>
  <div class="photo" role="img" aria-label="Portrait of the coach in a white blouse, smiling" style="left:302px;top:20px;width:180px;height:243px;background:linear-gradient(160deg,#e9e6e1,#b7b0a6 60%,#6e6a66)"></div>
  <div class="rule" style="left:0;top:118px;width:110px;background:var(--gray-web)"></div>
  <div class="heading abs" style="left:65px;top:80px;font-size:30px;font-weight:500">Welcome</div>
  <div class="abs" style="left:65px;top:140px;font-size:8.5px;color:var(--gray-web)">A Few Words About Carola</div>
  <div class="abs body-copy" style="left:65px;top:160px;width:180px;text-align:left;font-size:5.8px">Far far away, behind the word mountains, far from the countries Vokalia and Consonantia, there live the blind texts. Separated they live in Bookmarksgrove right at the coast of the Semantics, a large language ocean.</div>
  <div class="page" style="color:var(--white)">2</div>
</section>

<!-- Über mich -->
<section class="slide" style="left:314px;top:303.8px">
  <div class="abs" style="left:276px;top:0;width:224px;height:40px;background:var(--silver-sand)"></div>
  <div class="abs" style="left:276px;top:257px;width:224px;height:24px;background:var(--silver-sand)"></div>
  <div class="abs" style="left:151px;top:38px;width:349px;height:220px;background:var(--panel)"></div>
  <div class="brand" style="left:30px;top:34px;font-size:12px">dorneck-saalig</div>
  <div class="photo" role="img" aria-label="Coach resting her chin on her hand beside a plant" style="left:29px;top:89px;width:248px;height:192px;background:linear-gradient(135deg,#ece9e4,#c9c0b4 55%,#8b8a7d)"></div>
  <div class="abs" style="left:2px;top:226px;width:148px;height:30px;background:var(--gray-web);color:var(--white);font-size:8px;font-weight:700;display:flex;align-items:center;justify-content:center">A Few Words About Carola</div>
  <div class="heading abs" style="left:298px;top:122px;font-size:24px">Über Mich</div>
  <div class="quote abs" style="left:298px;top:170px;width:180px;font-size:8.5px;line-height:1.3">"Das Reisen in über 45 Ländern, Leben und Arbeiten auf mehreren Kontinenten und die Begegnung mit faszinierenden Kulturen hat mich tief geprägt."</div>
  <div class="page">3</div>
</section>

<!-- Meine Angebote -->
<section class="slide" style="left:612.5px;top:303.8px">
  <div class="abs" style="left:205px;top:0;width:295px;height:281px;background:var(--gray-soft)"></div>
  <div class="brand" style="right:28px;top:14px">dorneck-saalig</div>
  <div class="heading abs" style="left:23px;top:103px;font-size:19px;line-height:1.25">Meine<br>Angebote</div>
  <div class="rule" style="left:20px;top:158px;width:108px"></div>
  <div class="photo" role="img" aria-label="Compass on a rock at sunset" style="left:146px;top:57px;width:115px;height:165px;background:linear-gradient(180deg,#f4efe6,#d9b48f 55%,#6e655c)"></div>
  <div class="photo" role="img" aria-label="Hands working on a laptop" style="left:266px;top:57px;width:114px;height:165px;background:linear-gradient(160deg,#dfe6e8,#9cb0b6 60%,#c9a28f)"></div>
  <div class="photo" role="img" aria-label="Hand placing sticky notes on a wall" style="left:386px;top:57px;width:114px;height:165px;background:linear-gradient(160deg,#4f6b74,#d69a8a 55%,#f1d36a)"></div>
  <div class="abs" style="left:146px;top:228px;width:115px;text-align:center;font-size:7.5px;color:#333">Business Coaching</div>
  <div class="abs" style="left:266px;top:230px;width:114px;text-align:center;font-size:7.5px;color:#333">Strategische Beratung</div>
  <div class="abs" style="left:386px;top:230px;width:114px;text-align:center;font-size:7.5px;color:#333">Workshops &amp; Trainings</div>
  <div class="page">4</div>
</section>

<!-- Business Coaching -->
<section class="slide" style="left:16.3px;top:483.4px">
  <div class="abs" style="left:0;top:0;width:185px;height:172px;background:var(--powder-blue)"></div>
  <div class="brand" style="right:28px;top:14px">dorneck-saalig</div>
  <div class="photo" role="img" aria-label="Compass lying on a rock at sunrise" style="left:37px;top:47px;width:293px;height:234px;background:linear-gradient(180deg,#fbf6ee,#e6c9a7 50%,#6b5c51)"></div>
  <div class="heading abs" style="left:342px;top:78px;font-size:22px;line-height:1.3">Business<br>Coaching</div>
  <div class="rule" style="left:330px;top:140px;width:127px"></div>
  <div class="abs" style="left:277px;top:158px;width:204px;height:92px;background:var(--panel);box-shadow:0 2px 5px rgba(0,0,0,.15)"></div>
  <div class="abs" style="left:297px;top:175px;width:170px;font-size:7.5px;line-height:1.75;color:var(--gray-web)">"Zur authentischen Führung gehört vor allem auch die eigene Verletzlichkeit. Der Blick in den Spiegel. Und das braucht Mut!"</div>
  <div class="page">Page| 5</div>
</section>

<!-- Orientierung -->
<section class="slide" style="left:314px;top:483.4px">
  <div class="abs" style="left:340px;top:0;width:160px;height:281px;background:var(--gray-web)"></div>
  <div class="brand brand--light" style="right:28px;top:14px">dorneck-saalig</div>
  <div class="hashtag abs" style="left:37px;top:52px;font-size:20px">#Orientierung</div>
  <div class="rule" style="left:37px;top:78px;width:95px;background:var(--silver-sand)"></div>
  <div class="abs" style="left:37px;top:89px;font-size:9px;color:#444;font-weight:700">Neue Perspektiven entdecken.</div>
  <div class="abs body-copy" style="left:37px;top:104px;width:188px">Führung braucht heute einen klaren Blick nach vorn. Wer Teams durch Wandel begleitet, muss zuhören, Orientierung geben und Entscheidungen verständlich machen. Im Coaching schauen wir gemeinsam auf Ihre Rolle, Ihre Stärken und die nächsten Schritte. So entstehen neue Perspektiven, die im Alltag tragen und Ihre Wirkung als Führungskraft spürbar stärken.</div>
  <div class="abs body-copy" style="left:37px;top:232px;width:290px">Ein wertschätzender Coaching-Ansatz ist dabei der Schlüssel: Wir blicken auf das, was schon gelingt, und bauen darauf auf.</div>
  <div class="rule" style="left:241px;top:62px;width:1px;height:160px;background:var(--gray-web)"></div>
  <div class="photo" role="img" aria-label="Compass on a rock in warm evening light" style="left:243px;top:62px;width:210px;height:160px;background:linear-gradient(180deg,#f8f3ea,#e3c7a5 55%,#66594f)"></div>
  <div class="page" style="color:var(--white)">6</div>
</section>

<!-- Beratung -->
<section class="slide" style="left:612.5px;top:483.4px">
  <div class="brand" style="right:28px;top:14px">dorneck-saalig</div>
  <div class="heading abs" style="left:29px;top:40px;font-size:22px;color:var(--dim-gray)">Beratung</div>
  <div class="photo" role="img" aria-label="Two people discussing over a tablet at a desk" style="left:0;top:88px;width:500px;height:164px;background:linear-gradient(110deg,#2e4a5c,#c9d3d6 35%,#eef1f2 60%,#9fb5c4)"></div>
  <div class="abs" style="left:15px;top:125px;width:465px;height:58px;background:rgba(255,255,255,.55)"></div>
  <div class="quote abs" style="left:30px;top:141px;width:435px;text-align:center;font-size:7px;line-height:1.3">"Es ist vor allem die Kommunikation an die eigene Mannschaft, die in Veränderungsphasen ein – und oft sogar DAS – entscheidende Erfolgskriterium darstellt."</div>
  <div class="page">Page| 7</div>
</section>

<!-- Zukunft -->
<section class="slide" style="left:16.3px;top:663px">
  <div class="abs" style="left:377px;top:0;width:123px;height:281px;background:var(--silver-sand)"></div>
  <div class="hashtag abs" style="left:53px;top:30px;font-size:18px">#Zukunft</div>
  <div class="rule" style="left:48px;top:55px;width:90px"></div>
  <div class="photo" role="img" aria-label="Hands holding a tablet at a desk" style="left:284px;top:25px;width:192px;height:231px;background:linear-gradient(150deg,#e9edee,#c2cdd1 50%,#8d9ea5)"></div>
  <div class="abs" style="left:38px;top:68px;width:284px;height:45px;background:var(--panel-dark);box-shadow:0 2px 5px rgba(0,0,0,.15)"></div>
  <div class="abs" style="left:65px;top:84px;font-size:9px;color:#444">Wandel gestalten und Führung neu denken.</div>
  <div class="abs body-copy" style="left:43px;top:130px;width:207px;text-align:left">Als Kommunikationsexpertin begleite ich Inhaber, Geschäftsführer und Personalverantwortliche von Start-ups und Mittelstand. Gemeinsam entwickeln wir eine Führungskultur, die Veränderung nicht nur verwaltet, sondern aktiv gestaltet. Klare Kommunikation, ehrliches Feedback und Vertrauen sind dabei die Basis für nachhaltigen Erfolg im Unternehmen.</div>
  <div class="page">8</div>
</section>

<!-- Workshops & Trainings -->
<section class="slide" style="left:314px;top:663px">
  <div class="brand" style="left:17px;top:14px">dorneck-saalig</div>
  <div class="abs" style="left:0;top:193px;width:452px;height:88px;background:var(--powder-blue)"></div>
  <div class="rule" style="left:0;top:124px;width:105px"></div>
  <div class="photo" role="img" aria-label="Hands arranging colourful sticky notes" style="left:105px;top:35px;width:395px;height:122px;background:linear-gradient(110deg,#5a6f78,#c8b2ad 40%,#eec7b2 65%,#f3d36d)"></div>
  <div class="abs" style="left:132px;top:78px;font-family:'Playfair Display',serif;font-size:24px;color:var(--white);white-space:nowrap">Workshops &amp; Trainings</div>
  <div class="abs" style="left:103px;top:196px;width:397px;height:45px;background:var(--panel);box-shadow:0 2px 5px rgba(0,0,0,.15)"></div>
  <div class="abs" style="left:115px;top:206px;width:375px;text-align:center;font-size:6.5px;line-height:1.55;color:var(--gray-web)">"Führung heißt auch, sich zurücknehmen zu können. Es geht darum, Mitarbeiter/innen zur Eigenverantwortung zu befähigen, damit sie das Beste aus sich selbst herausholen können."</div>
  <div class="page">9</div>
</section>

<!-- Zusammenarbeit -->
<section class="slide" style="left:612.5px;top:663px">
  <div class="brand" style="left:17px;top:14px">dorneck-saalig</div>
  <div class="abs" style="left:0;top:75px;width:250px;height:206px;background:var(--powder-blue)"></div>
  <div class="photo" role="img" aria-label="Person with a coffee cup sorting sticky notes on glass" style="left:50px;top:40px;width:200px;height:202px;background:linear-gradient(150deg,#566c73,#c9a9a3 45%,#f0c4a8 70%,#f4d66e)"></div>
  <div class="abs" style="left:250px;top:20px;width:218px;height:240px;background:var(--silver-sand)"></div>
  <div class="hashtag abs" style="left:268px;top:38px;font-size:15px">#Zusammenarbeit</div>
  <div class="rule" style="left:262px;top:58px;width:200px;background:var(--white)"></div>
  <div class="abs" style="left:268px;top:64px;font-size:7.5px;color:#444">Stärkenorientiert und wertschätzend.</div>
  <div class="abs body-copy" style="left:268px;top:82px;width:190px;color:var(--white)">Seit vielen Jahren begleite ich Führungskräfte und Teams mit einem stärkenorientierten Blick. In Workshops und Trainings verbinde ich bewährte Methoden mit neuen Formaten der Zusammenarbeit. Im Mittelpunkt stehen Ihre Ressourcen, Ihre Ziele und eine Haltung, die Menschen ernst nimmt und Entwicklung möglich macht.</div>
  <div class="page">Page| 10</div>
</section>

<!-- Lernmomente -->
<section class="slide" style="left:16.3px;top:843px">
  <div class="photo" role="img" aria-label="Hiker crossing a suspension bridge in misty mountains" style="left:0;top:0;width:500px;height:213px;background:linear-gradient(180deg,#e9dcb6,#cbb98a 45%,#8a7f66 80%,#6d6656)"></div>
  <div class="abs" style="left:0;top:213px;width:250px;height:68px;background:var(--white)"></div>
  <div class="abs" style="left:250px;top:213px;width:250px;height:68px;background:var(--powder-blue)"></div>
  <div class="abs" style="left:32px;top:112px;font-family:'Montserrat',sans-serif;font-weight:500;font-size:22px;color:var(--white)">Lernmomente</div>
  <div class="abs" style="left:63px;top:155px;width:437px;height:55px;background:var(--panel)"></div>
  <div class="quote abs" style="left:80px;top:171px;width:405px;text-align:center;font-size:7px;line-height:1.5">"Krisen, die ich bewältigen und Fehler, die ich machen musste… unbezahlbare Lernmomente, die mich zu dem gemacht haben, was ich heute bin!"</div>
  <div class="brand" style="left:405px;top:236px">dorneck-saalig</div>
  <div class="page" style="color:var(--white)">11</div>
</section>

<!-- Erfahrungen -->
<section class="slide" style="left:314px;top:843px">
  <div class="abs" style="left:0;top:0;width:250px;height:281px;background:var(--gray-web)"></div>
  <div class="photo" role="img" aria-label="Misty mountain landscape with a suspension bridge" style="left:250px;top:0;width:250px;height:281px;background:linear-gradient(180deg,#8f8a78,#5d5a50 55%,#3f3d38)"></div>
  <div class="brand brand--light" style="right:28px;top:14px">dorneck-saalig</div>
  <div class="hashtag abs" style="left:35px;top:82px;font-size:18px">#Erfahrungen</div>
  <div class="abs" style="left:35px;top:107px;font-size:8px;color:var(--peach);font-weight:700">Sind da, um gemacht zu werden.</div>
  <div class="abs body-copy" style="left:35px;top:138px;width:198px;color:var(--champagne)">Meine Geschichte und mein beruflicher Weg sind alles andere als geradlinig. Jede Station hat mich geprägt, jede Herausforderung hat mich wachsen lassen. Heute gebe ich diese Erfahrungen weiter und unterstütze Sie dabei, Ihren eigenen Weg mit Klarheit und Mut zu gehen.</div>
  <ul class="abs" style="left:270px;top:135px;width:205px;font-size:5px;line-height:1.9;color:var(--white);font-weight:700;padding-left:6px">
    <li>Wie offen darf ich als Führungskraft sein?</li>
    <li>Wie treffe ich gute Entscheidungen unter Druck?</li>
    <li>Was bedeutet Authentizität in meiner Rolle?</li>
    <li>Wie führe ich in alle Richtungen zugleich?</li>
    <li>Wie verbinde ich Familie und Führung?</li>
  </ul>
  <div class="page" style="color:var(--white)">12</div>
</section>

<!-- Numbered list -->
<section class="slide" style="left:612.5px;top:843px">
  <div class="photo" role="img" aria-label="Coach in a white blouse looking upward outdoors" style="left:0;top:0;width:320px;height:281px;background:linear-gradient(150deg,#d8dcdc,#a9aeae 45%,#5a5b5d)"></div>
  <div class="brand" style="left:17px;top:14px">dorneck-saalig</div>
  <div class="abs" style="left:340px;top:48px;display:grid;grid-template-columns:38px 100px;row-gap:21px;align-items:center">
    <div class="heading" style="font-size:26px;font-weight:300">01</div><div style="font-size:5.5px;line-height:1.5;color:var(--gray-web)">Far far away, behind the word mountains, far from the countries Vokalia.</div>
    <div class="heading" style="font-size:26px;font-weight:300">02</div><div style="font-size:5.5px;line-height:1.5;color:var(--gray-web)">Far far away, behind the word mountains, far from the countries Vokalia.</div>
    <div class="heading" style="font-size:26px;font-weight:300">03</div><div style="font-size:5.5px;line-height:1.5;color:var(--gray-web)">Far far away, behind the word mountains, far from the countries Vokalia.</div>
    <div class="heading" style="font-size:26px;font-weight:300">04</div><div style="font-size:5.5px;line-height:1.5;color:var(--gray-web)">Far far away, behind the word mountains, far from the countries Vokalia.</div>
  </div>
  <div class="page">Page| 13</div>
</section>

<!-- Fakt ist -->
<section class="slide" style="left:16.3px;top:1023px">
  <div class="abs" style="left:0;top:0;width:170px;height:281px;background:var(--silver-sand)"></div>
  <div class="brand" style="right:28px;top:14px">dorneck-saalig</div>
  <div class="photo" role="img" aria-label="Coach sitting on sunlit steps outdoors" style="left:78px;top:29px;width:180px;height:223px;background:linear-gradient(160deg,#e9e0c8,#b4a88e 50%,#5a5349)"></div>
  <div class="abs" style="left:272px;top:40px;font-family:'Lato',sans-serif;font-size:19px;letter-spacing:1.3px;line-height:1.35;color:var(--dim-gray)">Fakt ist:<br>The hardest<br>person to lead<br>is yourself</div>
  <div class="rule" style="left:262px;top:165px;width:168px"></div>
  <div class="abs body-copy" style="left:273px;top:173px;width:172px;text-align:left">Selbstführung steht am Anfang guter Führung. Das habe ich selbst erst nach einigen Jahren meiner Karriere verstanden. Der ehrliche Blick in den Spiegel war oft unbequem, aber er hat mich weitergebracht. Genau diese Erfahrung teile ich heute als Coach und Beraterin.</div>
  <div class="page">Page| 14</div>
</section>

<!-- Place your title -->
<section class="slide" style="left:314px;top:1023px">
  <div class="brand" style="left:30px;top:14px">dorneck-saalig</div>
  <div class="photo" role="img" aria-label="Person with raised arm overlooking a blue lake and mountains" style="left:140px;top:0;width:360px;height:281px;background:linear-gradient(180deg,#3f79b8,#8fb4d6 35%,#4f6f8a 60%,#2f3b35)"></div>
  <div class="abs" style="left:43px;top:52px;width:192px;height:173px;background:var(--silver-sand);box-shadow:0 2px 6px rgba(0,0,0,.2)"></div>
  <div class="heading abs" style="left:70px;top:78px;font-size:20px;line-height:1.3;color:var(--dim-gray)">Place Your<br>Title here</div>
  <div class="rule" style="left:58px;top:142px;width:170px"></div>
  <div class="abs" style="left:63px;top:155px;width:155px;font-size:5.6px;line-height:1.6;color:var(--gray-web)">Far far away, behind the word mountains, far from the countries Vokalia and Consonantia, there live the blind texts. Separated they live in Bookmarksgrove.</div>
</section>

<!-- Text slide & image -->
<section class="slide" style="left:612.5px;top:1023px">
  <div class="abs" style="left:0;top:0;width:100px;height:60px;background:var(--silver-sand)"></div>
  <div class="abs" style="left:482px;top:0;width:18px;height:281px;background:var(--silver-sand)"></div>
  <div class="brand" style="right:28px;top:14px">dorneck-saalig</div>
  <div class="photo" role="img" aria-label="Person working at a desk with a monitor and a lettered sign" style="left:27px;top:60px;width:254px;height:221px;background:linear-gradient(140deg,#4a4f56,#9a8e7c 45%,#d9c58a 70%,#5d6a4f)"></div>
  <div class="abs" style="left:296px;top:96px;font-size:20px;letter-spacing:1.3px;line-height:1.35;color:var(--dim-gray)">Text Slide<br>&amp; Image</div>
  <div class="rule" style="left:281px;top:170px;width:169px"></div>
  <div class="abs" style="left:296px;top:195px;width:160px;font-size:5.6px;line-height:1.6;color:#444">Far far away, behind the word mountains, far from the countries Vokalia and Consonantia, there live the blind texts. Separated they live in Bookmarksgrove right at the coast of the Semantics, a large language ocean.</div>
  <div class="page">Page| 16</div>
</section>

</body>
</html>
```